Funky new Serviced Apartment Company needs a website + logo

Bright Harbor Serviced Lodging is a new company aiming to attract customers who need temporary accommodation (2 days to 6 months) in city locations.

Our customers make considerable savings on longer stays compared to hotels, and have all the creature comforts of home including super-fast WIFI, comfy beds, full kitchen and modern, yet comfortable, furniture.

Another key feature of the design is a page to attract "Partners" who "Work with Us" by allowing us to manage their properties and becoming part of our network of accommodation units. I have include a brochure from one of our competitors, and a video can be found here: http://lnkshort.example/clipz-7 - both can be used as I have permission.

The website design should work on all devices and screen sizes, and lend itself to a mobile app.

We would like to see website designs that are modern and simple, with a strong brand logo. The final design should communicate "Home From Home" and aim to attract professionals away from home on business for long periods of time.

Target Market(s)

Professional People working away from home for extended periods of time

Industry/Entity Type

Accommodation

Contact Information for Business Card

Name, Title, Phone Number, Email
Malcolm Ostby, Owner, 07831 562087, malcolm.ostby@brightharborsl.co.uk

Logo Text

Bright Harbor Service Lodging (Serviced Accommodation optional)

Coding

Coded - Design and coding required

Number of Pages Required

3 page

Font styles to use
Sans Serif

Requirements
Must have
• A 3 page website: Home, Partners, Contact Us
• Home page should have an area to list current apartment units, the user should be able to select a location and filter the list based on price and number of people.
• Partners page should inspire a "Work with us" call to action.
• The design should work with all screen sizes and devices.
• The design should say friendly and professional
Nice to have
• A simple logo, perhaps a smiling face made up using letters 'W' and 'H'.
• A neutral color scheme
Should not have
• No garish or vivid color scheme

```html
<!DOCTYPE html>
<html lang="en">
<head>
<meta charset="utf-8">
<title>Bright Harbor Serviced Lodging</title>
<link rel="stylesheet" href="https://fonts.googleapis.com/css2?family=Montserrat:wght@400;500;600;700&family=Open+Sans:wght@400;600;700&display=swap">
<style>
:root{
  --teal:#7f9ea3;
  --teal-dark:#5f7f86;
  --teal-soft:rgba(127,158,163,.78);
  --ink:#3f4346;
  --muted:#6a6f72;
  --line:#b9c6c9;
  --frame:#e4e6e6;
  --footer:#5c5e5a;
  --white:#ffffff;
}
*{margin:0;padding:0;box-sizing:border-box}
html,body{width:1200px;height:3352px;overflow:hidden}
body{background:var(--frame);font-family:"Open Sans",Arial,sans-serif;color:var(--ink);position:relative}
.page{position:absolute;left:16px;top:0;width:1168px;height:3335px;background:var(--white);overflow:hidden}
.abs{position:absolute}

/* top bar + header */
.topbar{left:0;top:0;width:1168px;height:50px;background:var(--teal)}
.topbar .contact-line{position:absolute;right:26px;top:14px;display:flex;gap:26px;align-items:center;color:#fff;font-size:14px;font-weight:600}
.topbar .contact-line span{display:flex;align-items:center;gap:8px}
.social{display:flex;gap:6px}
.social i{display:block;width:20px;height:20px;border:2px solid #fff;border-radius:50%}
.brand{left:26px;top:24px;display:flex;align-items:center;gap:14px}
.brand .dot{width:104px;height:104px;border-radius:50%;background:#fff;border:9px solid #555957}
.brand .name{font-family:"Montserrat",Arial,sans-serif;font-weight:600;color:#3c3f3d;font-size:29px;line-height:1.1;margin-top:44px}
.brand .name small{display:block;font-size:20px;font-weight:500;color:#3c3f3d}
.nav{right:28px;top:88px;display:flex;gap:28px;font-family:"Montserrat",Arial,sans-serif;font-size:14px;font-weight:600;color:#2f3336}

/* hero */
.hero{left:0;top:148px;width:1168px;height:580px}
.hero-photo{position:absolute;inset:0;background:
  radial-gradient(ellipse at 20% 30%,rgba(150,110,70,.75),rgba(150,110,70,0) 45%),
  linear-gradient(100deg,#bcc7cd 0%,#dfe5e8 40%,#eef1f2 70%,#e3e7e8 100%)}
.hero-cut{position:absolute;left:0;top:0;width:1168px;height:580px}
.hero-copy{left:700px;top:320px;width:430px}
.hero-copy h1{font-family:"Montserrat",Arial,sans-serif;font-size:19px;font-weight:600;letter-spacing:.5px;color:#3d4145;margin-bottom:20px}
.hero-copy p{font-size:14px;line-height:21px;color:#4e5356}
.btn{display:inline-block;background:var(--teal);color:#fff;font-family:"Montserrat",Arial,sans-serif;font-size:15px;font-weight:600;text-align:center;border-radius:5px;letter-spacing:.3px}
.hero-copy .btn{margin-top:18px;width:210px;height:36px;line-height:36px}

/* section headings */
.sec-head{display:flex;align-items:center;gap:16px;font-family:"Montserrat",Arial,sans-serif;font-size:22px;font-weight:600;color:var(--teal-dark);letter-spacing:.5px}
.sec-head .rule{width:120px;height:2px;background:var(--teal-dark)}
.sec-head .mark{width:36px;height:36px;border-radius:50%;border:3px solid var(--teal-dark)}

/* properties */
.props-head{left:372px;top:790px}
.filter{right:30px;top:790px;display:flex;align-items:center;gap:12px;font-family:"Montserrat",Arial,sans-serif;font-size:13px;font-weight:600;color:#333}
.card{width:362px;height:216px;border-radius:6px;overflow:hidden;box-shadow:0 2px 6px rgba(0,0,0,.25)}
.card .photo{position:absolute;inset:0}
.card .corner{position:absolute;right:0;top:0;width:60px;height:60px}
.card .label{position:absolute;left:0;bottom:0;width:100%;height:48px;background:var(--teal-soft);display:flex;align-items:center;justify-content:space-between;padding:0 18px;color:#fff;font-family:"Montserrat",Arial,sans-serif;font-size:13px;font-weight:600}
.card .label span{display:flex;align-items:center;gap:10px}
.card .label b{font-size:26px;font-weight:500}

/* partners */
.partners-photo{left:632px;top:1370px;width:536px;height:452px;background:linear-gradient(90deg,#fff 0%,#dde4e9 22%,#b8c3cc 55%,#8e98a2 100%)}
.partners-head{left:172px;top:1446px}
.partners-copy{left:26px;top:1512px;width:570px;font-size:14.8px;line-height:21px;color:#4a4f52}
.partners-btn{left:190px;top:1720px;width:212px;height:36px;line-height:36px}

/* why */
.why{left:0;top:1822px;width:1168px;height:760px}
.why-photo{position:absolute;inset:0;background:linear-gradient(180deg,#8aa7ad 0%,#9fb8bd 45%,#b9cbcf 100%)}
.why-head{left:428px;top:1886px;color:#fff}
.why-head .rule{background:#fff}
.why-head .mark{border-color:#fff}
.why-item{width:360px;display:flex;gap:18px}
.why-item .icon{flex:0 0 94px;height:94px;border-radius:50%;border:5px solid #555a5c;background:rgba(255,255,255,.15);display:flex;align-items:center;justify-content:center}
.why-item h3{font-family:"Montserrat",Arial,sans-serif;font-size:14.5px;font-weight:600;color:#fff;line-height:19px}
.why-item p{font-size:14.3px;line-height:19px;color:#fff}

/* contact */
.contact-head{left:396px;top:2508px}
.field{border:1px solid #c9cccd;border-radius:3px;background:#fff;font-family:"Montserrat",Arial,sans-serif;font-size:13px;font-weight:600;color:#333;padding:11px 14px}
.submit{left:478px;top:2794px;width:212px;height:36px;line-height:36px}

/* footer */
.footer{left:0;top:2899px;width:1168px;height:409px;background:var(--footer);color:#fff}
.footer .brand{left:18px;top:-10px}
.footer .brand .dot{border-color:var(--footer);width:120px;height:120px;border-width:12px}
.footer .brand .name{color:#fff;margin-top:36px}
.footer .brand .name small{color:#fff}
.fcol h4{font-family:"Montserrat",Arial,sans-serif;font-size:13.5px;font-weight:600;margin-bottom:24px}
.fcol ul{list-style:none;font-size:12.5px;line-height:22.5px}
.contact-row{display:flex;gap:12px;font-size:12.5px;line-height:20px;margin-bottom:20px}
.contact-row i{flex:0 0 16px;height:16px;border:2px solid #fff;border-radius:50%;margin-top:2px}
.copybar{left:0;top:3308px;width:1168px;height:27px;background:var(--teal);color:#fff;font-size:9.5px;font-weight:600;text-align:center;line-height:27px;letter-spacing:.4px}
</style>
</head>
<body>
<div class="page">

  <div class="abs topbar">
    <div class="contact-line">
      <span><svg width="16" height="16" viewBox="0 0 16 16"><circle cx="8" cy="8" r="7" fill="none" stroke="#fff" stroke-width="1.5"/><path d="M5.5 4.5l1.5 1.5-1 1c.5 1.2 1.3 2 2.5 2.5l1-1 1.5 1.5-1 1.2C7.5 11 5 8.5 4.5 5.5z" fill="#fff"/></svg>800.555.0142</span>
      <span><svg width="16" height="16" viewBox="0 0 16 16"><circle cx="8" cy="8" r="7" fill="none" stroke="#fff" stroke-width="1.5"/><rect x="4.5" y="5.5" width="7" height="5" fill="none" stroke="#fff"/><path d="M4.5 5.5l3.5 3 3.5-3" fill="none" stroke="#fff"/></svg>info@brightharbor.example</span>
      <span class="social"><i></i><i></i><i></i></span>
    </div>
  </div>

  <div class="abs brand">
    <div class="dot"></div>
    <div class="name">Bright Harbor<small>Serviced Lodging</small></div>
  </div>
  <nav class="abs nav"><span>Home</span><span>Partners</span><span>Why Bright Harbor</span><span>Contact Us</span></nav>

  <section class="abs hero">
    <div class="hero-photo" role="img" aria-label="Bedroom with wooden headboard, wall lamp and white pillows"></div>
    <svg class="hero-cut" viewBox="0 0 1168 580" preserveAspectRatio="none"><polygon points="0,400 510,580 0,580" fill="#fff"/><polygon points="510,580 1168,430 1168,580" fill="#fff"/><polyline points="0,400 510,580 1168,430" fill="none" stroke="#e3e6e7" stroke-width="3"/></svg>
  </section>
  <div class="abs hero-copy">
    <h1>BRIGHT HARBOR - SERVICE LODGING</h1>
    <p>We now offer a wide range of accommodation to meet our guest's needs and budget, with discounts available for longer stays. We have formed global partnerships with major corporates, and we pass on the benefits of these alliances to our landlords, in order that you may maximise your returns, with a minimum of hassle.</p>
    <span class="btn">BROWSE PROPERTIES</span>
  </div>

  <div class="abs sec-head props-head"><span class="rule"></span><span class="mark"></span>PROPERTIES<span class="rule"></span></div>
  <div class="abs filter"><svg width="40" height="34" viewBox="0 0 40 34"><g stroke="#333" stroke-width="2"><line x1="2" y1="5" x2="38" y2="5"/><line x1="2" y1="17" x2="38" y2="17"/><line x1="2" y1="29" x2="38" y2="29"/></g><g fill="#fff" stroke="#333" stroke-width="2"><circle cx="10" cy="5" r="3.5"/><circle cx="28" cy="17" r="3.5"/><circle cx="16" cy="29" r="3.5"/></g></svg>Filter Search</div>

  <div class="abs card" style="left:24px;top:872px">
    <div class="photo" role="img" aria-label="Bedroom with headboard and lamp" style="background:linear-gradient(110deg,#7a5a3e 0%,#a6b4bd 45%,#d9e1e6 100%)"></div>
    <svg class="corner" viewBox="0 0 60 60"><polygon points="0,0 60,0 60,60" fill="rgba(255,255,255,.55)"/><circle cx="44" cy="16" r="7" fill="none" stroke="#fff" stroke-width="2"/></svg>
    <div class="label"><span><svg width="16" height="22" viewBox="0 0 16 22"><path d="M8 1a7 7 0 0 0-7 7c0 5 7 13 7 13s7-8 7-13a7 7 0 0 0-7-7z" fill="#fff"/><circle cx="8" cy="8" r="2.6" fill="#7f9ea3"/></svg>Liverpool</span><span><b>£</b>Starts from 45.00</span></div>
  </div>
  <div class="abs card" style="left:403px;top:872px">
    <div class="photo" role="img" aria-label="Bright bedroom with large windows" style="background:linear-gradient(180deg,#e8e6e0 0%,#cfcac0 55%,#a99e8c 100%)"></div>
    <svg class="corner" viewBox="0 0 60 60"><polygon points="0,0 60,0 60,60" fill="rgba(255,255,255,.55)"/><circle cx="44" cy="16" r="7" fill="none" stroke="#fff" stroke-width="2"/></svg>
    <div class="label"><span><svg width="16" height="22" viewBox="0 0 16 22"><path d="M8 1a7 7 0 0 0-7 7c0 5 7 13 7 13s7-8 7-13a7 7 0 0 0-7-7z" fill="#fff"/><circle cx="8" cy="8" r="2.6" fill="#7f9ea3"/></svg>Manchester</span><span><b>£</b>Starts from 65.00</span></div>
  </div>
  <div class="abs card" style="left:782px;top:872px">
    <div class="photo" role="img" aria-label="Warm bedroom with ceiling light" style="background:linear-gradient(180deg,#e6d6bd 0%,#d3b993 55%,#b89a76 100%)"></div>
    <svg class="corner" viewBox="0 0 60 60"><polygon points="0,0 60,0 60,60" fill="rgba(255,255,255,.55)"/><circle cx="44" cy="16" r="7" fill="none" stroke="#fff" stroke-width="2"/></svg>
    <div class="label"><span><svg width="16" height="22" viewBox="0 0 16 22"><path d="M8 1a7 7 0 0 0-7 7c0 5 7 13 7 13s7-8 7-13a7 7 0 0 0-7-7z" fill="#fff"/><circle cx="8" cy="8" r="2.6" fill="#7f9ea3"/></svg>Wrigley</span><span><b>£</b>Starts from 35.00</span></div>
  </div>
  <div class="abs card" style="left:24px;top:1102px">
    <div class="photo" role="img" aria-label="Living room with sofas and chandelier" style="background:linear-gradient(180deg,#c9a77a 0%,#a5825a 55%,#7d6142 100%)"></div>
    <svg class="corner" viewBox="0 0 60 60"><polygon points="0,0 60,0 60,60" fill="rgba(255,255,255,.55)"/><circle cx="44" cy="16" r="7" fill="none" stroke="#fff" stroke-width="2"/></svg>
    <div class="label"><span><svg width="16" height="22" viewBox="0 0 16 22"><path d="M8 1a7 7 0 0 0-7 7c0 5 7 13 7 13s7-8 7-13a7 7 0 0 0-7-7z" fill="#fff"/><circle cx="8" cy="8" r="2.6" fill="#7f9ea3"/></svg>Tottenham</span><span><b>£</b>Starts from 35.00</span></div>
  </div>
  <div class="abs card" style="left:403px;top:1102px">
    <div class="photo" role="img" aria-label="Empty room with dark walls and doorway" style="background:linear-gradient(180deg,#6a6c6b 0%,#8f8e89 55%,#a79c8a 100%)"></div>
    <svg class="corner" viewBox="0 0 60 60"><polygon points="0,0 60,0 60,60" fill="rgba(255,255,255,.55)"/><circle cx="44" cy="16" r="7" fill="none" stroke="#fff" stroke-width="2"/></svg>
    <div class="label"><span><svg width="16" height="22" viewBox="0 0 16 22"><path d="M8 1a7 7 0 0 0-7 7c0 5 7 13 7 13s7-8 7-13a7 7 0 0 0-7-7z" fill="#fff"/><circle cx="8" cy="8" r="2.6" fill="#7f9ea3"/></svg>London</span><span><b>£</b>Starts from 95.00</span></div>
  </div>
  <div class="abs card" style="left:782px;top:1102px">
    <div class="photo" role="img" aria-label="Light bedroom with white bedding" style="background:linear-gradient(180deg,#eef0ef 0%,#e1e3e1 55%,#cfd3d1 100%)"></div>
    <svg class="corner" viewBox="0 0 60 60"><polygon points="0,0 60,0 60,60" fill="rgba(255,255,255,.55)"/><circle cx="44" cy="16" r="7" fill="none" stroke="#fff" stroke-width="2"/></svg>
    <div class="label"><span><svg width="16" height="22" viewBox="0 0 16 22"><path d="M8 1a7 7 0 0 0-7 7c0 5 7 13 7 13s7-8 7-13a7 7 0 0 0-7-7z" fill="#fff"/><circle cx="8" cy="8" r="2.6" fill="#7f9ea3"/></svg>London</span><span><b>£</b>Starts from 95.00</span></div>
  </div>

  <div class="abs partners-photo" role="img" aria-label="Two businessmen shaking hands across a desk"></div>
  <div class="abs sec-head partners-head"><span class="rule"></span><span class="mark"></span>PARTNERS</div>
  <p class="abs partners-copy">We will spend time getting to know you and your serviced apartment, meaning we offer a bespoke personal service. Whether you need help furnishing and dressing your property, arranging cleaning services or anything in between, we can help. Then we'll talk to your customers, work out what makes them tick and get them excited about booking your property. We deliver the same personalised service to both customers and owners - meaning we give them a memorable booking experience, build customer loyalty and get them to holiday with us and you - time and again.</p>
  <span class="abs btn partners-btn">WORK WITH US</span>

  <section class="abs why">
    <div class="why-photo" role="img" aria-label="Bedroom interior with ceiling fan under a soft teal wash"></div>
    <svg class="abs" style="left:0;top:560px" width="1168" height="200" viewBox="0 0 1168 200" preserveAspectRatio="none"><polygon points="0,192 670,28 1168,176 1168,200 0,200" fill="#fff"/><polyline points="0,192 670,28 1168,176" fill="none" stroke="#e3e6e7" stroke-width="3"/></svg>
  </section>
  <div class="abs sec-head why-head"><span class="rule"></span><span class="mark"></span>WHY BRIGHT HARBOR<span class="rule"></span></div>

  <div class="abs why-item" style="left:18px;top:1962px">
    <div class="icon"><svg width="50" height="50" viewBox="0 0 50 50"><rect x="6" y="10" width="32" height="32" fill="none" stroke="#555a5c" stroke-width="4"/><path d="M14 24l9 9 20-24" fill="none" stroke="#555a5c" stroke-width="5"/></svg></div>
    <div><h3>Regular bookings, regular payments</h3><p>Our specialists constantly assess the booking trends in your area so we can provide you with a simple pricing structure which is perfect for your property, designed to sell it at its best rate and attract year round booking.</p></div>
  </div>
  <div class="abs why-item" style="left:398px;top:1962px">
    <div class="icon"><svg width="46" height="46" viewBox="0 0 46 46"><rect x="5" y="8" width="36" height="32" rx="3" fill="none" stroke="#555a5c" stroke-width="4"/><line x1="5" y1="16" x2="41" y2="16" stroke="#555a5c" stroke-width="4"/><g fill="#555a5c"><rect x="11" y="21" width="6" height="5"/><rect x="20" y="21" width="6" height="5"/><rect x="29" y="21" width="6" height="5"/><rect x="11" y="30" width="6" height="5"/><rect x="20" y="30" width="6" height="5"/><rect x="29" y="30" width="6" height="5"/></g></svg></div>
    <div><h3>Managing your bookings</h3><p>From dealing with customers day-to-day queries and processing bookings, to ensuring payments reach you on time every month, we'll take care of all the hard work and finer detail, so you don't have to.</p></div>
  </div>
  <div class="abs why-item" style="left:778px;top:1962px">
    <div class="icon"><svg width="46" height="46" viewBox="0 0 46 46"><path d="M9 7l8 8-5 5c3 6 8 11 14 14l5-5 8 8-5 6C20 41 5 26 3 12z" fill="#555a5c"/></svg></div>
    <div><h3>Expert support from the start</h3><p>Your local manager and our in-house team will be by your side at every step of your letting journey. Whenever you need us - all you have to do is pick up the phone!</p></div>
  </div>
  <div class="abs why-item" style="left:18px;top:2180px">
    <div class="icon"><svg width="46" height="46" viewBox="0 0 46 46"><text x="23" y="34" text-anchor="middle" font-family="Montserrat,Arial,sans-serif" font-size="32" font-weight="700" fill="#555a5c">£</text></svg></div>
    <div><h3>Maximize your income</h3><p>Your local manager offers extensive experience and expertise in your property's market, whilst our in-house pricing analysts constantly review your area's seasonal booking trends.</p></div>
  </div>
  <div class="abs why-item" style="left:398px;top:2180px">
    <div class="icon"><svg width="46" height="46" viewBox="0 0 46 46"><rect x="6" y="9" width="28" height="30" fill="none" stroke="#555a5c" stroke-width="4"/><path d="M18 32l3-8 16-16 5 5-16 16z" fill="#555a5c"/></svg></div>
    <div><h3>You'll be in control</h3><p>Need to block out time at your property? That's fine by us, all we ask is that you keep us in the loop so we can keep your availability calendar up to date - conditions apply on usage (contact us to discuss).</p></div>
  </div>
  <div class="abs why-item" style="left:778px;top:2180px">
    <div class="icon"><svg width="46" height="46" viewBox="0 0 46 46"><path d="M23 40S5 29 5 17a9 9 0 0 1 18-3 9 9 0 0 1 18 3c0 12-18 23-18 23z" fill="none" stroke="#555a5c" stroke-width="4"/></svg></div>
    <div><h3>Your peace of mind</h3><p>With over 10 years experience successfully managing serviced accommodation just like yours, you can be confident that we know how to get the best results for you and your property.</p></div>
  </div>

  <div class="abs sec-head contact-head"><span class="rule"></span><span class="mark"></span>CONTACT US<span class="rule"></span></div>
  <div class="abs field" style="left:100px;top:2588px;width:313px;height:45px">Your Name</div>
  <div class="abs field" style="left:427px;top:2588px;width:313px;height:45px">Your Email</div>
  <div class="abs field" style="left:755px;top:2588px;width:313px;height:45px">Your Subject</div>
  <div class="abs field" style="left:100px;top:2648px;width:968px;height:132px">Message</div>
  <span class="abs btn submit">SUBMIT</span>

  <footer class="abs footer">
    <div class="abs brand"><div class="dot"></div><div class="name">Bright Harbor<small>Serviced Lodging</small></div></div>
    <div class="abs fcol" style="left:156px;top:134px"><h4>QUICK LINKS</h4><ul><li>Home</li><li>About</li><li>Partners</li><li>Why Bright Harbor</li><li>Contact Us</li></ul></div>
    <div class="abs fcol" style="left:382px;top:134px"><h4>SERVICE AREAS</h4><ul><li>Greater Manchester</li><li>Essex</li><li>Lancashire</li><li>Nottinghamshire</li><li>Hertfordshire</li><li>Somerset</li><li>Cheshire</li><li>Cambridgeshire</li></ul></div>
    <div class="abs fcol" style="left:566px;top:180px"><ul><li>Cardiff</li><li>Oxfordshire</li><li>Berkshire</li><li>Surrey</li><li>Derbyshire</li><li>Devon</li><li>Yorkshire</li><li>Hampshire</li></ul></div>
    <div class="abs fcol" style="left:733px;top:134px"><h4>CONTACT</h4>
      <div class="contact-row"><i></i><div>Bright Harbor Serviced Lodging<br>48 Quayside Row<br>Unit 7</div></div>
      <div class="contact-row"><i></i><div>1880.555.0199</div></div>
      <div class="contact-row"><i></i><div>hello@brightharbor.example</div></div>
    </div>
  </footer>
  <div class="abs copybar">© COPYRIGHT 2017 BRIGHT HARBOR SERVICED LODGING. ALL RIGHTS RESERVED</div>

</div>
</body>
</html>
```